PeakVoyageHub

1. Can you describe what your company does?

Please find enclosed documents for your reference about our business doing.

2. Who are your target customers for the website?

Company Positioning: A comprehensive supplier of premier international sports travel and high-end event services.
Core Advantage: Exclusive international partnership resources and an Official Ticketing Assurance System.
Service Standard: One-Stop, High-Quality Service Solutions based on the "An once-in-a-lifetime experience" philosophy.

Our target customers for the website:
Mid-to-High-end Sports Enthusiasts
Corporate Clients
Sports Associations
Please kindly find enclosed for more details about our target customers, I think it's very important to make it clear to you.

3. Do you have an existing domain name / website address?

Yes, I have. I just applied for this new domain and it's totally a new website. www.peakvoyagehub.example

4. In addition to a Home Page, which other pages / sections would you like your website to have:
About Us
Contact Us , Office / Mailing Address
Sports Travel Products( Bucket Lists) : Globe Shield, Crown Quartet, Panathlia, Football, Courtline, Golf, Skiing, Hiking,Galas
Reviews/ Unforgettable Moments
FAQs
Any other page / section you would like: Here is the website for your reference, www.lanejaunts.example
For each of the pages / sections you’d like to have, please provide the text (and images, if available) you would like to include.
Please recommend 2-3 templates to me, and let me know what kind of text I will provide to every web pages.

5. Which of the below are features and functionalities your website will need:
Image Gallery
Videos
Contact Form
Maps
FAQs
6. Please provide the URLs for the social media profiles you'd like to link to the website.

Do you know Quiet Blue Ledger?

Please let me know anything you need, thank you very much!

Have a good day!

Target Market(s)

Travel for the world-wide sports games and make an once-in-a-lifetime experience

Industry/Entity Type

sports and travel industry

Coding

Coded - Design and coding required

Number of Pages Required

5+ page

Requirements
Must have
• our logo
Nice to have
• On the homepage, I’d like a banner-style section to prominently showcase the latest products.

```html
<!DOCTYPE html>
<html lang="en">
<head>
<meta charset="utf-8">
<title>PeakVoyageHub – Sports Travel</title>
<link rel="stylesheet" href="https://fonts.googleapis.com/css2?family=Merriweather:ital,wght@0,700;1,700&family=Lato:wght@400;700&display=swap">
<style>
:root{
  --navy:#0c3e6c;
  --navy-deep:#0a355e;
  --ink:#2b2f36;
  --muted:#4a5059;
  --sky:#e4f1fa;
  --line:#d4dbe3;
  --white:#ffffff;
  --star:#f4a61b;
}
*{box-sizing:border-box;margin:0;padding:0}
html,body{width:1200px;height:4142px;overflow:hidden}
body{font-family:"Lato",sans-serif;color:var(--ink);background:var(--white)}
.wrap{width:980px;margin:0 auto;position:relative}
h2.section-title{font-family:"Merriweather",serif;font-weight:700;color:var(--navy);font-size:37px;text-align:center}
.btn{display:inline-flex;align-items:center;justify-content:center;background:var(--navy);color:var(--white);font-weight:700;font-size:17px;border-radius:26px;text-decoration:none}

/* header */
.site-header{height:85px}
.site-header .wrap{display:flex;align-items:center;justify-content:space-between;height:85px}
.brand{display:flex;align-items:center;gap:12px;color:var(--navy);font-family:"Merriweather",serif;font-weight:700;font-size:25px}
.brand-dot{width:56px;height:56px;border-radius:50%;border:3px solid var(--navy)}
.main-nav{display:flex;gap:27px;font-size:15px}
.main-nav a{color:var(--ink);text-decoration:none}

/* hero */
.hero{height:512px;position:relative;background:linear-gradient(180deg,#9fb2c2 0%,#7d93a8 35%,#4f6478 62%,#2f3a43 100%);text-align:center;color:var(--white)}
.hero h1{padding-top:50px;font-family:"Merriweather",serif;font-weight:700;font-size:50px;text-shadow:0 2px 6px rgba(0,0,0,.35)}
.hero h1 em{font-style:italic}
.hero p{margin-top:18px;font-size:17px;line-height:26px;font-weight:700}
.hero .btn{margin-top:32px;width:172px;height:46px;border:2px solid var(--white);font-size:16px}

/* about */
.about{height:613px}
.about .photo-a{position:absolute;left:1px;top:85px;width:375px;height:348px;border-radius:16px;background:linear-gradient(160deg,#5b7a3a,#2f4d24 60%,#b9a88a)}
.about .photo-b{position:absolute;left:165px;top:257px;width:325px;height:278px;border-radius:16px;background:linear-gradient(180deg,#486b86 0%,#c9a76a 55%,#3d3524 100%)}
.about-copy{position:absolute;left:533px;top:78px;width:447px}
.about-copy h2{font-family:"Merriweather",serif;color:var(--navy);font-size:36px;margin-left:2px}
.about-copy p{margin-top:14px;font-size:14px;line-height:26px;text-align:justify;color:var(--muted)}
.points{list-style:none;margin-top:8px}
.points li{display:flex;gap:14px;font-size:14px;line-height:26px;text-align:justify;color:var(--muted);margin-bottom:6px}
.points svg{flex:0 0 20px;margin-top:3px}
.points b{color:var(--ink)}
.about-copy .btn{margin-top:12px;width:137px;height:46px}

/* products */
.products{height:897px;background:var(--sky);padding-top:76px}
.product-grid{display:grid;grid-template-columns:repeat(3,304px);gap:28px 34px;margin-top:26px}
.product-card{height:279px;border-radius:12px;position:relative;overflow:hidden}
.product-card span{position:absolute;left:0;right:0;bottom:0;padding:30px 0 12px;text-align:center;color:var(--white);font-family:"Merriweather",serif;font-weight:700;font-size:20px;background:linear-gradient(180deg,rgba(12,62,108,0),rgba(12,62,108,.9))}
.products .center{text-align:center;margin-top:28px}
.products .btn{width:137px;height:46px}

/* planner form */
.planner{height:576px;padding-top:72px}
.plan-form{display:grid;grid-template-columns:449px 449px;gap:20px 42px;margin:34px 0 0 20px}
.field{height:48px;border:1px solid var(--line);border-radius:6px;box-shadow:0 2px 5px rgba(0,0,0,.08);display:flex;align-items:center;padding:0 20px;gap:12px;font-size:14px;color:#6b717a}
.field .chev{margin-left:auto}
.planner .center{text-align:center;margin-top:30px}
.planner .btn{width:211px;height:46px}

/* testimonials */
.reviews{height:531px;background:var(--sky);padding-top:72px}
.review-row{display:grid;grid-template-columns:repeat(3,309px);gap:26px;margin-top:30px}
.review-card{height:297px;background:var(--white);border:1px solid var(--line);border-radius:10px;padding:22px 20px 0}
.stars{display:flex;gap:2px}
.review-card h3{font-weight:400;font-size:16px;margin-top:12px;color:var(--ink)}
.review-card p{font-size:15px;line-height:25px;color:var(--muted);margin-top:8px;height:75px;overflow:hidden}
.review-card a{font-size:14px;font-style:italic;color:var(--muted)}
.reviewer{display:flex;align-items:center;gap:20px;margin-top:16px}
.avatar{width:76px;height:76px;border-radius:50%;background:linear-gradient(160deg,#c8b6a0,#6d5a48)}
.reviewer strong{display:block;font-size:18px;color:var(--ink)}
.reviewer small{font-size:14px;color:var(--ink)}
.arrow{position:absolute;top:166px;width:28px;height:28px}

/* faq */
.faq{height:558px;padding-top:72px}
.faq-list{position:absolute;left:-1px;top:87px;width:560px;list-style:none}
.faq-list li{height:52px;border:1px solid var(--line);border-radius:6px;box-shadow:0 2px 5px rgba(0,0,0,.07);display:flex;align-items:center;justify-content:space-between;padding:0 22px 0 36px;font-size:14px;margin-bottom:14px}
.faq-video{position:absolute;left:617px;top:87px;width:361px;height:307px;border-radius:16px;background:linear-gradient(180deg,#c9d2d8 0%,#7f95a8 45%,#405a73 75%,#2c3f51 100%)}
.faq-video svg{position:absolute;right:22px;top:22px}

/* footer */
.site-footer{height:370px;background:var(--navy-deep);color:var(--white)}
.site-footer .brand{color:var(--white);position:absolute;left:0;top:95px}
.site-footer .brand-dot{border-color:var(--white)}
.socials{position:absolute;left:2px;top:206px;display:flex;gap:16px}
.socials span{width:22px;height:22px;border-radius:50%;background:var(--white)}
.foot-col{position:absolute;top:90px}
.foot-col h4{font-size:20px;font-weight:700;margin-bottom:18px}
.foot-col ul{list-style:none}
.foot-col li{font-size:14px;height:34px;display:flex;align-items:flex-start;gap:14px}
.foot-col li::before{content:"";width:7px;height:7px;border-radius:50%;background:var(--white);margin-top:5px}
.foot-col.contact li{height:auto;margin-bottom:22px;line-height:24px}
.foot-col.contact li::before{display:none}
.foot-col.contact svg{flex:0 0 18px;margin-top:3px}
.foot-rule{position:absolute;left:3px;right:0;top:323px;border-top:1px solid rgba(255,255,255,.3)}
.copyright{position:absolute;left:0;right:0;top:341px;text-align:center;font-size:14px}
</style>
</head>
<body>

<header class="site-header">
  <div class="wrap">
    <div class="brand"><span class="brand-dot"></span>PeakVoyageHub</div>
    <nav class="main-nav">
      <a href="#">Home</a><a href="#">About</a><a href="#">Sports Travel Packages</a><a href="#">Testimonials</a><a href="#">FAQs</a><a href="#">Contact Us</a>
    </nav>
  </div>
</header>

<section class="hero" role="img" aria-label="Hiker standing on a rocky summit above a misty mountain valley">
  <h1>Travel the World <em>Live the Game</em></h1>
  <p>From the Panathlia to the Globe Shield — discover tailor-made<br>experiences that bring your passion for sport to life.</p>
  <a class="btn" href="#">Discover Events</a>
</section>

<section class="about">
  <div class="wrap">
    <div class="photo-a" role="img" aria-label="Group of hikers on a forest trail"></div>
    <div class="photo-b" role="img" aria-label="Hikers with poles on a ridge at sunset"></div>
    <div class="about-copy">
      <h2>About Us</h2>
      <p>Our company has been deeply rooted in the sports and high-end service sector for over a decade, with businesses covering High-end Conference Management and Planning, Sports Event Operation, and, at its core, Sports Travel services.</p>
      <ul class="points">
        <li><svg width="20" height="20" viewBox="0 0 20 20"><circle cx="10" cy="10" r="10" fill="#0c3e6c"/><path d="M5 10h9M10 6l4 4-4 4" stroke="#fff" stroke-width="2" fill="none"/></svg><span><b>Professional Qualification:</b> Holds an Outbound Travel Operating License issued by the National Tourism Administration, providing legal and reliable international travel service guarantees for clients.</span></li>
        <li><svg width="20" height="20" viewBox="0 0 20 20"><circle cx="10" cy="10" r="10" fill="#0c3e6c"/><path d="M5 10h9M10 6l4 4-4 4" stroke="#fff" stroke-width="2" fill="none"/></svg><span><b>Resource Advantage:</b> Established deep partnerships with numerous large foreign sports organizations and associations to ensure clients secure scarce, official tickets for premier international events.</span></li>
      </ul>
      <a class="btn" href="#">Read More</a>
    </div>
  </div>
</section>

<section class="products">
  <div class="wrap">
    <h2 class="section-title">Sports Travel Products</h2>
    <div class="product-grid">
      <div class="product-card" role="img" aria-label="Golden trophy on a dark stage" style="background:linear-gradient(160deg,#1d2a38,#0e1620 60%,#7a5a1c)"><span>Globe Shield</span></div>
      <div class="product-card" role="img" aria-label="Tennis racket and ball in a packed stadium" style="background:linear-gradient(180deg,#b8c7d2,#5e7d93 50%,#2f4f66)"><span>Crown Quartet</span></div>
      <div class="product-card" role="img" aria-label="Flag waving above a city" style="background:linear-gradient(180deg,#7fb1dc,#dfe9f1 45%,#6f8ea6)"><span>Panathlia</span></div>
      <div class="product-card" role="img" aria-label="Boot striking a football on grass" style="background:linear-gradient(160deg,#3c4650,#1b2228 55%,#4f5b3b)"><span>Football</span></div>
      <div class="product-card" role="img" aria-label="Gloved hand placing a golf ball on a tee" style="background:linear-gradient(180deg,#c9a14d,#7b7a35 50%,#2e4a24)"><span>Golf</span></div>
      <div class="product-card" role="img" aria-label="Hiker with backpack facing a tall peak" style="background:linear-gradient(180deg,#a9b8c4,#6f8496 50%,#33414d)"><span>Hiking</span></div>
    </div>
    <div class="center"><a class="btn" href="#">Read More</a></div>
  </div>
</section>

<section class="planner">
  <div class="wrap">
    <h2 class="section-title">Let’s Plan Your Ultimate Sports Experience</h2>
    <form class="plan-form">
      <div class="field"><svg width="18" height="18" viewBox="0 0 18 18"><circle cx="9" cy="5" r="4" fill="#7a8089"/><path d="M1 17c0-5 16-5 16 0z" fill="#7a8089"/></svg>Name</div>
      <div class="field"><svg width="18" height="18" viewBox="0 0 18 18"><circle cx="9" cy="9" r="8" fill="none" stroke="#7a8089" stroke-width="2"/><path d="M1 9h16M9 1c-4 4-4 12 0 16M9 1c4 4 4 12 0 16" stroke="#7a8089" fill="none"/></svg>Country / Region<svg class="chev" width="12" height="8" viewBox="0 0 12 8"><path d="M1 1l5 5 5-5" stroke="#444" stroke-width="1.6" fill="none"/></svg></div>
      <div class="field"><svg width="18" height="14" viewBox="0 0 18 14"><rect x="1" y="1" width="16" height="12" rx="1" fill="none" stroke="#7a8089" stroke-width="2"/><path d="M1 1l8 7 8-7" stroke="#7a8089" stroke-width="2" fill="none"/></svg>Email</div>
      <div class="field"><svg width="18" height="18" viewBox="0 0 18 18"><path d="M3 1l4 1 1 4-2 2c1 2 3 4 5 5l2-2 4 1 1 4-2 1C8 17 1 10 2 3z" fill="#7a8089"/></svg>Phone Number</div>
      <div class="field"><svg width="18" height="18" viewBox="0 0 18 18"><rect x="1" y="3" width="16" height="14" rx="2" fill="#7a8089"/><rect x="3" y="8" width="12" height="7" fill="#fff"/></svg>Select Your Interested Event<svg class="chev" width="12" height="8" viewBox="0 0 12 8"><path d="M1 1l5 5 5-5" stroke="#444" stroke-width="1.6" fill="none"/></svg></div>
      <div class="field"><svg width="18" height="18" viewBox="0 0 18 18"><rect x="1" y="3" width="16" height="14" rx="2" fill="none" stroke="#7a8089" stroke-width="2"/><path d="M1 7h16" stroke="#7a8089" stroke-width="2"/></svg>Travel Dates<svg class="chev" width="12" height="8" viewBox="0 0 12 8"><path d="M1 1l5 5 5-5" stroke="#444" stroke-width="1.6" fill="none"/></svg></div>
      <div class="field"><svg width="22" height="16" viewBox="0 0 22 16"><circle cx="11" cy="4" r="3.5" fill="#7a8089"/><circle cx="4" cy="6" r="2.5" fill="#7a8089"/><circle cx="18" cy="6" r="2.5" fill="#7a8089"/><path d="M5 16c0-6 12-6 12 0zM0 16c0-4 6-5 6-2v2zM22 16c0-4-6-5-6-2v2z" fill="#7a8089"/></svg>Number of Travelers<svg class="chev" width="12" height="8" viewBox="0 0 12 8"><path d="M1 1l5 5 5-5" stroke="#444" stroke-width="1.6" fill="none"/></svg></div>
      <div class="field"><svg width="20" height="18" viewBox="0 0 20 18"><ellipse cx="10" cy="8" rx="9" ry="7" fill="#7a8089"/><path d="M4 13l-2 4 6-3z" fill="#7a8089"/></svg>Message</div>
    </form>
    <div class="center"><a class="btn" href="#">Submit</a></div>
  </div>
</section>

<section class="reviews">
  <div class="wrap">
    <h2 class="section-title">Unforgettable Moments from Our Travelers</h2>
    <svg class="arrow" style="left:-55px" viewBox="0 0 28 28"><circle cx="14" cy="14" r="13" fill="none" stroke="#555"/><path d="M16 9l-5 5 5 5" stroke="#555" stroke-width="1.6" fill="none"/></svg>
    <svg class="arrow" style="right:-70px" viewBox="0 0 28 28"><circle cx="14" cy="14" r="13" fill="none" stroke="#222"/><path d="M12 9l5 5-5 5" stroke="#222" stroke-width="1.6" fill="none"/></svg>
    <div class="review-row">
      <article class="review-card">
        <div class="stars"><svg width="92" height="17" viewBox="0 0 92 17"><g fill="#f4a61b"><path id="s" d="M8.5 0l2.5 5.5 6 .6-4.5 4 1.3 6-5.3-3.1-5.3 3.1 1.3-6L0 6.1l6-.6z"/><use href="#s" x="19"/><use href="#s" x="38"/><use href="#s" x="57"/><use href="#s" x="76"/></g></svg></div>
        <h3>“Globe Shield Magic!”</h3>
        <p>Our Globe Shield experience was beyond expectation. From official tickets to VIP hospitality</p>
        <a href="#">Read More</a>
        <div class="reviewer"><div class="avatar" role="img" aria-label="Portrait of traveler Owen R."></div><div><strong>Owen R.,</strong><small>United Kingdom</small></div></div>
      </article>
      <article class="review-card">
        <div class="stars"><svg width="92" height="17" viewBox="0 0 92 17"><g fill="#f4a61b"><use href="#s"/><use href="#s" x="19"/><use href="#s" x="38"/><use href="#s" x="57"/><use href="#s" x="76"/></g></svg></div>
        <h3>“Corporate Trip Done Right.”</h3>
        <p>We arranged a client hospitality package for the Eastern Open through PeakVoyageHub. The level of</p>
        <a href="#">Read More</a>
        <div class="reviewer"><div class="avatar" role="img" aria-label="Portrait of traveler Priya K." style="background:linear-gradient(160deg,#b58d6a,#4b3428)"></div><div><strong>Priya K.,</strong><small>Singapore</small></div></div>
      </article>
      <article class="review-card">
        <div class="stars"><svg width="92" height="17" viewBox="0 0 92 17"><g fill="#f4a61b"><use href="#s"/><use href="#s" x="19"/><use href="#s" x="38"/><use href="#s" x="57"/><use href="#s" x="76"/></g></svg></div>
        <h3>“Panathlia Dreams Realized.”</h3>
        <p>Attending the Panathlia was my lifelong dream. PeakVoyageHub made it effortless — from</p>
        <a href="#">Read More</a>
        <div class="reviewer"><div class="avatar" role="img" aria-label="Portrait of traveler Tomas B." style="background:linear-gradient(160deg,#9aa4ad,#3c3f44)"></div><div><strong>Tomas B.,</strong><small>Canada</small></div></div>
      </article>
    </div>
  </div>
</section>

<section class="faq">
  <div class="wrap">
    <h2 class="section-title">Frequently Asked Questions</h2>
    <ul class="faq-list">
      <li>1. Are your tickets official and guaranteed?<svg width="16" height="16" viewBox="0 0 16 16"><circle cx="8" cy="8" r="7" fill="none" stroke="#444"/><path d="M8 4v8M4 8h8" stroke="#444"/></svg></li>
      <li>2. Can I customize my sports travel package?<svg width="16" height="16" viewBox="0 0 16 16"><circle cx="8" cy="8" r="7" fill="none" stroke="#444"/><path d="M8 4v8M4 8h8" stroke="#444"/></svg></li>
      <li>3. Do you organize trips for corporate groups or VIP guests?<svg width="16" height="16" viewBox="0 0 16 16"><circle cx="8" cy="8" r="7" fill="none" stroke="#444"/><path d="M8 4v8M4 8h8" stroke="#444"/></svg></li>
      <li>4. What if an event is postponed or rescheduled?<svg width="16" height="16" viewBox="0 0 16 16"><circle cx="8" cy="8" r="7" fill="none" stroke="#444"/><path d="M8 4v8M4 8h8" stroke="#444"/></svg></li>
      <li>5. Do you provide on-site assistance during events?<svg width="16" height="16" viewBox="0 0 16 16"><circle cx="8" cy="8" r="7" fill="none" stroke="#444"/><path d="M8 4v8M4 8h8" stroke="#444"/></svg></li>
    </ul>
    <div class="faq-video" role="img" aria-label="Video still of a hiker overlooking layered blue mountain ridges">
      <svg width="30" height="30" viewBox="0 0 30 30"><circle cx="15" cy="15" r="15" fill="#3a3f45"/><path d="M12 9l9 6-9 6z" fill="#fff"/></svg>
    </div>
  </div>
</section>

<footer class="site-footer">
  <div class="wrap" style="height:370px">
    <div class="brand"><span class="brand-dot"></span>PeakVoyageHub</div>
    <div class="socials"><span></span><span></span><span></span><span></span></div>
    <div class="foot-col" style="left:323px">
      <h4>Quick Links</h4>
      <ul><li>Home</li><li>About</li><li>Sports Travel Packages</li><li>Testimonials</li><li>FAQs</li></ul>
    </div>
    <div class="foot-col" style="left:556px">
      <h4>Popular Events</h4>
      <ul><li>Globe Shield</li><li>Panathlia</li><li>Lawnfield Open</li><li>Azalea Classic</li><li>Courtline Finals</li></ul>
    </div>
    <div class="foot-col contact" style="left:776px">
      <h4>Contact Us</h4>
      <ul>
        <li><svg width="18" height="18" viewBox="0 0 18 18"><path d="M9 1a6 6 0 0 1 6 6c0 5-6 10-6 10S3 12 3 7a6 6 0 0 1 6-6z" fill="#fff"/><circle cx="9" cy="7" r="2.2" fill="#0a355e"/></svg><span>88 Harbor Lane, Suite 4,<br>Brookfield, NY 10990</span></li>
        <li><svg width="18" height="18" viewBox="0 0 18 18"><circle cx="9" cy="9" r="9" fill="#fff"/><rect x="4" y="6" width="10" height="7" fill="#0a355e"/></svg><span>info@peakvoyagehub.example</span></li>
        <li><svg width="18" height="18" viewBox="0 0 18 18"><circle cx="9" cy="9" r="9" fill="#fff"/><path d="M6 4l2 .5.5 2-1 1c.6 1.2 1.5 2 2.5 2.5l1-1 2 .5.5 2-1 .8C9 13 5 9 5.2 5z" fill="#0a355e"/></svg><span>+1 555 010 2040</span></li>
      </ul>
    </div>
    <div class="foot-rule"></div>
    <p class="copyright">© 2025 PeakVoyageHub. All Rights Reserved.</p>
  </div>
</footer>

</body>
</html>
```